Design some Business Cards for Fern Basket Shop

I need a clean and clear cooperate, but represents green and high ethics business card. This card will be printed on plantable paper. Please open the attached files for the templates and size I want my card to be. And also use the attached logo. Details one the card are

email: contact@fernbasketshop.example
Name: Karim Al-Hadrawi
Position: Director
Number: 07622487531
Address: Studio 14, Vale Works, Penmore Street, Sheffield, S7 9LX, United Kingdom
Web: www.fernbasketshop.example

```html
<!DOCTYPE html>
<html lang="en">
<head>
<meta charset="utf-8">
<title>Fern Basket Shop – Business Cards</title>
<link href="https://fonts.googleapis.com/css2?family=Open+Sans:wght@300;400;600&display=swap" rel="stylesheet">
<style>
  :root {
    --bg: #ece9e4;
    --card: #ffffff;
    --green: #5cbf2a;
    --green-dark: #2f7a12;
    --icon: #5c5c5c;
    --ink: #6b6b6b;
    --white: #ffffff;
  }
  * { margin: 0; padding: 0; box-sizing: border-box; }
  html, body { width: 1200px; height: 912px; overflow: hidden; }
  body {
    background: var(--bg);
    font-family: "Open Sans", sans-serif;
    position: relative;
  }
  .card {
    position: absolute;
    width: 540px;
    height: 308px;
    background: var(--card);
    box-shadow: 0 10px 28px rgba(0,0,0,0.14);
    overflow: hidden;
  }
  .card--front { left: 70px; top: 130px; }
  .card--back { left: 590px; top: 474px; }

  .card__panel { position: absolute; inset: 0; }

  .holder { position: absolute; left: 34px; top: 38px; color: var(--white); }
  .holder__name { font-size: 21px; font-weight: 400; letter-spacing: 0.2px; line-height: 1.2; }
  .holder__role { font-size: 12px; font-weight: 400; color: var(--green-dark); margin-top: 2px; }

  .contact { position: absolute; left: 34px; top: 118px; width: 236px; list-style: none; }
  .contact__item {
    color: var(--white);
    font-size: 11px;
    font-weight: 400;
    line-height: 1.4;
    padding: 6px 0 5px;
    border-bottom: 1px solid rgba(255,255,255,0.75);
  }

  .brand {
    position: absolute;
    display: flex;
    align-items: center;
    gap: 10px;
  }
  .brand__dot { width: 22px; height: 22px; border-radius: 50%; background: var(--green); flex: none; }
  .brand__name { font-size: 24px; font-weight: 600; color: var(--ink); white-space: nowrap; }
  .card--front .brand { right: 36px; top: 30px; }
  .card--back .brand { left: 50%; top: 112px; transform: translateX(-50%); }

  .card__web {
    position: absolute;
    right: 110px;
    bottom: 96px;
    font-size: 11.5px;
    color: #333;
  }
</style>
</head>
<body>
  <section class="card card--front" aria-label="Business card front">
    <svg class="card__panel" width="540" height="308" viewBox="0 0 540 308">
      <polygon points="0,0 232,0 410,308 0,308" fill="var(--green)"/>
      <g class="contact-icons">
        <rect x="262" y="96" width="44" height="32" fill="var(--icon)"/>
        <path d="M275 114 L284 106 L293 114 M278 113 V121 H290 V113" fill="none" stroke="#fff" stroke-width="2"/>
        <rect x="310" y="132" width="44" height="32" fill="var(--icon)"/>
        <path d="M324 139 q-3 3 2 10 q5 7 9 5 l2-3 -4-3 -2 2 q-3-2-5-6 l2-2 -3-4z" fill="#fff"/>
        <rect x="358" y="168" width="44" height="32" fill="var(--icon)"/>
        <rect x="370" y="175" width="20" height="13" fill="none" stroke="#fff" stroke-width="2"/>
        <path d="M367 192 H393" stroke="#fff" stroke-width="2"/>
      </g>
    </svg>
    <div class="holder">
      <p class="holder__name">Karim Al-Hadrawi</p>
      <p class="holder__role">Director</p>
    </div>
    <ul class="contact">
      <li class="contact__item">Studio 14, Vale Works, Penmore Street, Sheffield, S7 9LX, United Kingdom</li>
      <li class="contact__item">07622487531</li>
      <li class="contact__item">contact@fernbasketshop.example</li>
      <li class="contact__item">www.fernbasketshop.example</li>
    </ul>
    <div class="brand">
      <span class="brand__dot"></span>
      <span class="brand__name">Fern Basket Shop</span>
    </div>
  </section>

  <section class="card card--back" aria-label="Business card back">
    <div class="brand">
      <span class="brand__dot"></span>
      <span class="brand__name">Fern Basket Shop</span>
    </div>
    <p class="card__web">www.fernbasketshop.example</p>
  </section>
</body>
</html>
```